Business Card Design

Take existing logo/brand and develop business card for sales team.
We have two separate brands and require a business card for each.

1. VoxHarbor
2. MyNimbusLinko

Refer to our websites www.voxharbor.com.au and www.mynimbuslinko.com.au for designs currently implemented and in the marketplace.

Both cards are brands of our parent company Quorvane Systems Pty Ltd - an Australian Telecommunications company in the medium business sector. We have only business customers, no retail/residential consumers.

Target Market(s)

Australian Business - small to medium enterprise

Industry/Entity Type

Business

Contact Information for Business Card

Ted Ramsell
Sales Director
Mobile: +61 428 163 907
Direct: +61 3 9172 5836
Email: ted@voxharbor.com.au
VoxHarbor (a brand of Quorvane Systems Pty Ltd)

Ted Ramsell
Sales Director
Mobile: +61 428 163 907
Direct: +61 3 9172 5836
Email: ted@mynimbuslinko.com.au
MyNimbusLinko (a brand of Quorvane Systems Pty Ltd)

Font styles to use
Sans Serif
Other font styles liked:
• Roboto Condensed, Open Sans

Requirements
Must have
• Clean lines, crisp fonts - suggest Roboto Condensed or similar.
• Must be easy to read and clear.
• Brand colour #0C8CCD
• Two colour maximum
Nice to have
• Modern, intellectual and unique design.
Should not have
• No die cuts
• No copies or rip-offs of other designs

```html
<!DOCTYPE html>
<html lang="en">
<head>
<meta charset="utf-8">
<title>VoxHarbor Business Cards</title>
<link rel="stylesheet" href="https://fonts.googleapis.com/css2?family=Source+Sans+3:wght@300;400;600&display=swap">
<style>
  :root {
    --brand: #0c8ccd;
    --brand-text: #1a86c7;
    --ink: #3d3d3d;
    --ink-soft: #555555;
    --rule: #c8c8c8;
    --paper: #f7f7f7;
    --stage: #8a8a8a;
    --white: #ffffff;
  }
  * { margin: 0; padding: 0; box-sizing: border-box; }
  html, body {
    width: 1200px;
    height: 750px;
    overflow: hidden;
  }
  body {
    background: var(--stage);
    font-family: "Source Sans 3", sans-serif;
    position: relative;
  }
  .card {
    position: absolute;
    width: 492px;
    height: 281px;
    background: var(--paper);
  }
  .card--front-sales { left: 75px; top: 69px; }
  .card--front-ceo { left: 630px; top: 65px; }
  .card--back {
    left: 352px; top: 403px;
    background: var(--brand);
  }

  .brand-lockup {
    position: absolute;
    left: 0; right: 0;
    top: 46px;
    height: 70px;
    display: flex;
    align-items: center;
    justify-content: center;
    gap: 12px;
  }
  .brand-mark {
    width: 62px; height: 62px;
    border-radius: 50%;
    background: var(--brand);
  }
  .brand-name {
    font-weight: 300;
    font-size: 46px;
    color: var(--brand);
    letter-spacing: 0.5px;
    line-height: 1;
  }
  .card--back .brand-lockup { top: 92px; }
  .card--back .brand-mark { background: var(--white); }
  .card--back .brand-name { color: var(--white); }

  .holder {
    position: absolute;
    top: 152px;
    right: 288px;
    text-align: right;
  }
  .holder__name {
    font-size: 18px;
    font-weight: 600;
    color: var(--brand-text);
    line-height: 1.2;
  }
  .holder__title {
    font-size: 13px;
    color: var(--ink);
    margin-top: 5px;
  }
  .card--front-ceo .holder { right: 274px; }

  .divider {
    position: absolute;
    top: 147px;
    left: 228px;
    width: 1px;
    height: 52px;
    background: var(--rule);
  }
  .card--front-ceo .divider { left: 242px; }

  .contacts {
    position: absolute;
    top: 146px;
    left: 248px;
    list-style: none;
  }
  .card--front-ceo .contacts { left: 262px; }
  .contacts li {
    display: flex;
    align-items: center;
    gap: 7px;
    height: 19px;
    font-size: 12.5px;
    color: var(--ink-soft);
  }
  .contacts svg { width: 13px; height: 13px; fill: var(--brand); flex: none; }

  .company-line {
    position: absolute;
    left: 0; right: 0;
    top: 245px;
    display: flex;
    align-items: center;
    justify-content: center;
    gap: 4px;
    font-size: 13px;
    font-weight: 600;
    color: var(--brand-text);
  }
  .card--front-ceo .company-line { top: 242px; }
  .company-line::before,
  .company-line::after {
    content: "";
    width: 58px;
    height: 2px;
  }
  .company-line::before { background: linear-gradient(to right, transparent, var(--brand)); }
  .company-line::after { background: linear-gradient(to left, transparent, var(--brand)); }

  .web-line {
    position: absolute;
    left: 0; right: 0;
    top: 232px;
    display: flex;
    align-items: center;
    justify-content: center;
    gap: 4px;
    font-size: 12px;
    letter-spacing: 2.6px;
    color: var(--white);
  }
  .web-line::before,
  .web-line::after {
    content: "";
    width: 36px;
    height: 1px;
  }
  .web-line::before { background: linear-gradient(to right, transparent, var(--white)); }
  .web-line::after { background: linear-gradient(to left, transparent, var(--white)); }
</style>
</head>
<body>

<section class="card card--front-sales" aria-label="Business card front, Ted Ramsell">
  <div class="brand-lockup">
    <span class="brand-mark"></span>
    <span class="brand-name">voxharbor</span>
  </div>
  <div class="holder">
    <p class="holder__name">Ted Ramsell</p>
    <p class="holder__title">Sales Director</p>
  </div>
  <span class="divider"></span>
  <ul class="contacts">
    <li><svg viewBox="0 0 16 16" aria-hidden="true"><path d="M1 5c0-2 3-3 7-3s7 1 7 3v1h-3.5V4.5h-7V6H1zM4 7h8l2 6H2zm4 1.5a2 2 0 1 0 0 4 2 2 0 0 0 0-4z"/></svg>+61 3 9172 5836</li>
    <li><svg viewBox="0 0 16 16" aria-hidden="true"><path d="M4.5 0h7A1.5 1.5 0 0 1 13 1.5v13a1.5 1.5 0 0 1-1.5 1.5h-7A1.5 1.5 0 0 1 3 14.5v-13A1.5 1.5 0 0 1 4.5 0zM5 2v10.5h6V2zm3 11.2a.9.9 0 1 0 0 1.8.9.9 0 0 0 0-1.8z"/></svg>+61 428 163 907</li>
    <li><svg viewBox="0 0 16 16" aria-hidden="true"><path d="M1 4h14v9H1zm1.5 1.2v.4L8 9.4l5.5-3.8v-.4zM2.5 7.3v4.4h11V7.3L8 11.1z"/></svg>ted@voxharbor.com.au</li>
  </ul>
  <p class="company-line">Quorvane Systems Pty Ltd</p>
</section>

<section class="card card--front-ceo" aria-label="Business card front, Alan Corbett">
  <div class="brand-lockup">
    <span class="brand-mark"></span>
    <span class="brand-name">voxharbor</span>
  </div>
  <div class="holder">
    <p class="holder__name">Alan Corbett</p>
    <p class="holder__title">CEO</p>
  </div>
  <span class="divider"></span>
  <ul class="contacts">
    <li><svg viewBox="0 0 16 16" aria-hidden="true"><path d="M1 5c0-2 3-3 7-3s7 1 7 3v1h-3.5V4.5h-7V6H1zM4 7h8l2 6H2zm4 1.5a2 2 0 1 0 0 4 2 2 0 0 0 0-4z"/></svg>+61 2 8463 2190</li>
    <li><svg viewBox="0 0 16 16" aria-hidden="true"><path d="M4.5 0h7A1.5 1.5 0 0 1 13 1.5v13a1.5 1.5 0 0 1-1.5 1.5h-7A1.5 1.5 0 0 1 3 14.5v-13A1.5 1.5 0 0 1 4.5 0zM5 2v10.5h6V2zm3 11.2a.9.9 0 1 0 0 1.8.9.9 0 0 0 0-1.8z"/></svg>+61 437 912 648</li>
    <li><svg viewBox="0 0 16 16" aria-hidden="true"><path d="M1 4h14v9H1zm1.5 1.2v.4L8 9.4l5.5-3.8v-.4zM2.5 7.3v4.4h11V7.3L8 11.1z"/></svg>alanc@voxharbor.com.au</li>
  </ul>
  <p class="company-line">Quorvane Systems Pty Ltd</p>
</section>

<section class="card card--back" aria-label="Business card back">
  <div class="brand-lockup">
    <span class="brand-mark"></span>
    <span class="brand-name">voxharbor</span>
  </div>
  <p class="web-line">www.voxharbor.com.au</p>
</section>

</body>
</html>
```